Industrial Professional Business Card Design (Vantrel Systems)

Would like professional looking business cards. Not too busy leaning towards minimal. Should have a slogan like:
"Industrial Automation and Control".

We are a tech company that programs industrial PLC computers. We also develop custom hardware solutions. Please use the logo for inspiration.

Target Market(s)

Mining, industrial, processing, automation, factory

Industry/Entity Type

Engineering

Contact Information for Business Card

Name, phone, email, website. job title.

Font styles to use
Other font styles liked:
• droid sans

Requirements
Must have
• Use colours that go well with the logo. Not too busy design.

```html
<!DOCTYPE html>
<html lang="en">
<head>
<meta charset="utf-8">
<title>Vantrel Systems — Business Card</title>
<link rel="stylesheet" href="https://fonts.googleapis.com/css2?family=Noto+Sans:wght@400;600&display=swap">
<style>
  :root {
    --backdrop: #d4d5d7;
    --orange: #ec6824;
    --paper-light: #fafbfc;
    --paper-dark: #e8e6e7;
    --navy: #1d3a5f;
    --accent-blue: #1f5f86;
    --white: #ffffff;
  }
  html, body {
    margin: 0;
    padding: 0;
    width: 1200px;
    height: 1200px;
    overflow: hidden;
    background: var(--backdrop);
    font-family: "Noto Sans", sans-serif;
  }
  .canvas {
    position: relative;
    width: 1200px;
    height: 1200px;
  }
  .card {
    position: absolute;
    width: 724px;
    height: 436px;
    display: block;
  }
  .card--front { left: 101px; top: 115px; }
  .card--back  { left: 405px; top: 652px; }
  .card text { font-family: "Noto Sans", sans-serif; }
  .holder-name { font-size: 32px; fill: var(--white); }
  .holder-title { font-size: 17px; fill: var(--white); }
  .contact-line { font-size: 19px; fill: var(--white); }
  .slogan { font-size: 16px; font-weight: 600; fill: var(--orange); }
  .brand-name { font-size: 25px; font-weight: 400; fill: var(--navy); }
</style>
</head>
<body>
<main class="canvas">

  <!-- Front: holder details -->
  <svg class="card card--front" viewBox="0 0 724 436" role="group" aria-label="Business card front">
    <defs>
      <linearGradient id="front-paper" x1="0" x2="1" y1="0" y2="0">
        <stop offset="0" stop-color="var(--paper-dark)"/>
        <stop offset="0.4" stop-color="#eae7e8"/>
        <stop offset="0.75" stop-color="var(--paper-light)"/>
      </linearGradient>
      <filter id="front-hex-shadow" x="-20%" y="-20%" width="150%" height="150%">
        <feDropShadow dx="6" dy="0" stdDeviation="7" flood-color="#8a3a10" flood-opacity="0.35"/>
      </filter>
    </defs>
    <rect class="card-paper" width="724" height="436" fill="url(#front-paper)"/>
    <polygon class="card-band" points="326,0 724,0 724,436 326,436 302,356 381,219 300,82" fill="var(--orange)"/>
    <polygon class="name-hexagon" points="143,82 300,82 381,219 302,356 143,356 64,219" fill="var(--orange)" filter="url(#front-hex-shadow)"/>

    <text class="holder-name" x="129" y="212">Your Name</text>
    <text class="holder-title" x="130" y="230">Designation</text>
    <rect class="title-rule" x="130" y="242" width="181" height="2" fill="var(--white)"/>
    <rect class="title-rule-accent" x="130" y="241" width="32" height="4" fill="var(--accent-blue)"/>

    <g class="contact-icons" fill="var(--white)">
      <path class="icon-phone" d="M413,180 c2,-2 4,-2 5,0 l3,4 c1,2 0,3 -1,4 l-1,1 c1,3 4,6 7,7 l1,-1 c1,-1 2,-2 4,-1 l4,3 c2,1 2,3 0,5 l-2,2 c-3,2 -10,-1 -15,-6 c-5,-5 -8,-12 -6,-15 z"/>
      <g class="icon-mail">
        <rect x="412" y="215" width="21" height="14" fill="var(--white)"/>
        <path d="M412,215 l10.5,8 l10.5,-8" fill="none" stroke="var(--orange)" stroke-width="1.4"/>
        <path d="M412,229 l8,-7 M433,229 l-8,-7" stroke="var(--orange)" stroke-width="1.2"/>
      </g>
      <path class="icon-cursor" d="M417,245 l0,18 l4,-4 l3,7 l3,-1 l-3,-7 l6,0 z"/>
    </g>
    <text class="contact-line" x="458" y="193">xxx-xxxxxx-xxx</text>
    <text class="contact-line" x="458" y="227">hello@vantrelsystems.com</text>
    <text class="contact-line" x="458" y="261">www.vantrelsystems.com</text>
  </svg>

  <!-- Back: brand and slogan -->
  <svg class="card card--back" viewBox="0 0 724 436" role="group" aria-label="Business card back">
    <defs>
      <linearGradient id="back-paper" x1="0" x2="1" y1="0" y2="0">
        <stop offset="0" stop-color="var(--paper-light)"/>
        <stop offset="1" stop-color="#efeeef"/>
      </linearGradient>
      <linearGradient id="back-hex-paper" x1="0" x2="1" y1="0" y2="0">
        <stop offset="0" stop-color="var(--paper-light)"/>
        <stop offset="1" stop-color="var(--paper-dark)"/>
      </linearGradient>
      <filter id="back-hex-shadow" x="-20%" y="-20%" width="150%" height="150%">
        <feDropShadow dx="-6" dy="0" stdDeviation="7" flood-color="#000" flood-opacity="0.18"/>
      </filter>
    </defs>
    <rect class="card-paper" width="724" height="436" fill="url(#back-paper)"/>
    <polygon class="card-band" points="401,0 724,0 724,436 398,436 424,356 582,356 661,219 582,83 425,83" fill="var(--orange)"/>
    <polygon class="brand-hexagon" points="425,83 582,83 661,219 582,356 424,356 344,219" fill="url(#back-hex-paper)" filter="url(#back-hex-shadow)"/>

    <text class="slogan" x="189" y="225" text-anchor="middle">"Industrial Automation and Control"</text>

    <circle class="brand-dot" cx="504" cy="198" r="14" fill="var(--orange)"/>
    <text class="brand-name" x="504" y="252" text-anchor="middle">Vantrel Systems</text>
  </svg>

</main>
</body>
</html>
```